Vast Ledger Web Design - For local online shopping 'village'

URGENTLY REQUIRE WEB DESIGNER FOR VAST LEDGER WEB STORE - CODING REQUIRED

REQUIREMENT; BE ABLE TO TALK ENGLISH VERY WELL AS THIS WILL BE AN ON GOING PROJECT

(WE WILL BE TALKING ON TALKLOOM OR CHIRPLINE)

The business name is 'Holmwyck's - Corvale's Online Shopping Village'
(PICS ATTACHED FOR LAYOUT DEMONSTRATION PURPOSES)

I need a draft of the website operational within 7 days to show potential clients. The remainder may take an additional 7+ days to complete. Can discuss further payments due to the work involved.

It's an online shopping village where individual shop owners have the ability to place their store (logo) and their products on this website to increase exposure to their business and more importantly their online delivery service.

The site will need to be structured in a very easy to use manner. Customers ages will range from 18+ to 80+.

THE IMAGINATION, FEEL & PRESENCE OF THE WEB PAGE;
You are a professional web designer, I will need you to use your imagination and add pieces to this website that I can't see. My vision and feel for this website is based on the grocery stores that were able to survive and thrive during the late stages of WWII. A lot of design now and with future marketing & advertising will be revolved and the 1940's feel & look. I'm happy to hear your thoughts on things we can add or improve on in the site. It's very basic now and it's more warmth and character.

THE LAYOUT;
The first page will have a white brick wallpaper background (pic attached as 'wallpaper'. This will be the wallpaper used for the entire site. The business logo (hasn't been made yet - waiting on drafts) will be at the top of the page and beneath it will be 3 categories to choose from (in the final stage it will have 6 categories).

DRAFT STAGE;
1. Village grocers (pic attached ' vgrocers') (To be written ' Village Grocers written on the frame burnt into the wood or written underneath the frame - must be large and clear to read')
2. Butchers (pic attached 'vbutcher')(as above - Village butchers)
3. Seafood (pic attached 'VSF')(as above Seafood)
They will all require framing (pic attached 'frame')
I'd like the images to be slightly bouncy if you put your mouse or finger on the logo.

Once the customer enters their choice it will then take them to their desired category.

NEXT PAGE:

Main focus is in the Grocers section; The same design structure will appear (business logo 'Holmwyck - Corvale's online shopping village'.
2 business choices will be available in this section. Their logos are attached ('PDNQ' and 'Mundey's Grocer') I'd like you to enhance the logo's with more depth and background shadow - please don't spend to much time but make them look better. I'd like the logo's to be slightly bouncy if you put your mouse or finger on the logo. The wallpaper used will be 'wallpaper'.

PLEASE NOTE: Could you please remove the logo from the background image of 'PDNQ'.

For the draft stage we will focus on 'PDNQ'. Once you click on PDNQ it will take you to their page. The wallpaper will be the same as the brick wallpaper on the other 2 pages. The logo of 'PDNQ' will be placed boldly at the top middle of the page. On this page there will be 4 categories to choose from. Everything will be the same, wallpaper will be white brick, the categories (pics attached as Deli, Fruit&Veg, Bakery & Pantry ) they will need to be framed and the category name will be burnt into the wood or placed underneath.

This is where we stop for the time being.

I've attached layout pictures, so you can see what I see. Please add all the little things i've added to the layout pictures that i haven't written here..

Example: Our Mission, Contact us, Home delivery.. etc.

The site will need to continue to grow as we fill the categories with products and add more businesses to the site.. so on and so on. It's an ongoing job and we will need good communication and understanding with each other.

Please do what you can to show your vision in line with what i've written above. If you'd like to contact me feel free to do so, we can organize a talk on talkloom if need be.

All the best & I hope you are all safe and healthy!

Odo

Industry/Entity Type

Online Store

Coding

Coded - Design and coding required

Number of Pages Required

5+ page

Requirements
Must have
• Looks like the 1940's merged with the modern age.
Nice to have
• Age some nice grocery store touches. 1940's + grocery stores had things hanging from the walls, ornaments here and there. It felt homely. Add some things or talk about the things that you're thinking about adding.

```html
<!DOCTYPE html>
<html lang="en">
<head>
<meta charset="utf-8">
<title>Holmwyck – Corvale's Online Shopping Village</title>
<link rel="stylesheet" href="https://fonts.googleapis.com/css2?family=Poppins:wght@500;600;700&display=swap">
<style>
  :root{
    --ink:#1c1c1c;
    --paper:#ffffff;
    --wall-a:#f4f4f2;
    --wall-b:#e7e7e4;
    --rule:#8a8a8a;
    --wood-dark:#5a3a1f;
    --wood-mid:#7b5331;
    --wood-light:#9a6c42;
    --brand-orange:#f08a34;
    --brand-green:#2f7d3a;
  }
  *{box-sizing:border-box;margin:0;padding:0}
  html,body{width:1200px;height:2531px;overflow:hidden;background:var(--paper)}
  body{position:relative;font-family:"Poppins",sans-serif;color:var(--ink)}

  .page-label{position:absolute;left:0;width:1200px;text-align:center;font-weight:700;font-size:17px;letter-spacing:.3px}
  .page{position:absolute;left:0;width:1200px;overflow:hidden;
    background:
      radial-gradient(ellipse at 30% 20%, rgba(255,255,255,.8), transparent 60%),
      radial-gradient(ellipse at 80% 70%, rgba(255,255,255,.6), transparent 55%),
      linear-gradient(180deg,var(--wall-b),var(--wall-a) 40%,var(--wall-b));
  }

  .brand{position:absolute;left:0;width:1200px;text-align:center}
  .brand-name{font-weight:700;font-size:40px;line-height:1;letter-spacing:1px;color:var(--ink)}
  .brand-tagline{margin-top:12px;font-weight:600;font-size:16px;letter-spacing:.5px;color:var(--ink);text-transform:uppercase}

  .frame{position:absolute;width:310px;height:236px;background:var(--wood-mid);border-radius:3px}
  .frame::before,.frame::after{content:"";position:absolute;left:-4px;right:-4px;height:40px;background:var(--wood-light);border-radius:2px}
  .frame::before{top:4px}
  .frame::after{bottom:2px;background:var(--wood-dark)}
  .frame-post{position:absolute;top:0;bottom:0;width:30px;background:var(--wood-dark)}
  .frame-post.left{left:10px}
  .frame-post.right{right:10px}
  .frame-photo{position:absolute;left:40px;top:42px;right:42px;bottom:43px;z-index:1}
  .photo-grocers{background:linear-gradient(135deg,#1e2126,#3f6b2c 40%,#e0833a 60%,#1e2126)}
  .photo-butchers{background:linear-gradient(180deg,#c98b86,#7c3a39 45%,#222326)}
  .photo-seafood{background:linear-gradient(135deg,#7fa3c3,#c1473a 45%,#3e5f80)}
  .photo-deli{background:linear-gradient(90deg,#a8403a,#c68b80 40%,#9a6a45 60%,#b07b50)}
  .photo-fruitveg{background:linear-gradient(135deg,#3a5a2c,#d7b835 45%,#c9452a 70%,#2f3a28)}
  .photo-bakery{background:linear-gradient(135deg,#5a3a22,#c8955a 50%,#6e4a2c)}
  .photo-pantry{background:linear-gradient(180deg,#3a2418,#b35a2c 45%,#7a8a3a 70%,#3a2418)}

  .category-name{position:absolute;width:310px;text-align:center;font-weight:700;font-size:17px;text-transform:uppercase}

  .site-footer{position:absolute;left:0;width:1200px;height:140px;border-top:1px solid var(--rule)}
  .footer-links{position:absolute;top:40px;list-style:none}
  .footer-links li{font-weight:600;font-size:12.5px;line-height:30px;text-transform:uppercase}
  .footer-links.left{left:235px}
  .footer-links.right{left:852px}
  .footer-brand{position:absolute;top:48px;left:0;width:1200px;text-align:center}
  .footer-brand .brand-name{font-size:26px}
  .footer-brand .brand-tagline{margin-top:4px;font-size:11px}

  .store-mark{position:absolute;display:flex;align-items:center;gap:14px;font-weight:700;transform:translate(-50%,-50%)}
  .store-mark .mark-square{width:40px;height:40px;background:var(--brand-orange)}
  .store-mark .mark-circle{width:70px;height:70px;border-radius:50%;background:var(--brand-green)}
  .store-pdnq{color:var(--brand-orange);font-size:46px}
  .store-mundey{color:var(--brand-green);font-size:30px;flex-direction:column;gap:10px}
</style>
</head>
<body>

  <!-- Home -->
  <div class="page-label" style="top:44px">PAGE 1</div>
  <section class="page" style="top:100px;height:626px">
    <div class="brand" style="top:46px">
      <div class="brand-name">HOLMWYCK</div>
      <div class="brand-tagline">Corvale's Online Shopping Village</div>
    </div>

    <div class="frame" style="left:95px;top:160px"><span class="frame-post left"></span><span class="frame-post right"></span><div class="frame-photo photo-grocers" role="img" aria-label="Crate of fresh vegetables and fruit"></div></div>
    <div class="frame" style="left:446px;top:160px"><span class="frame-post left"></span><span class="frame-post right"></span><div class="frame-photo photo-butchers" role="img" aria-label="Raw cuts of meat on a board"></div></div>
    <div class="frame" style="left:797px;top:160px"><span class="frame-post left"></span><span class="frame-post right"></span><div class="frame-photo photo-seafood" role="img" aria-label="Fresh seafood on ice"></div></div>

    <div class="category-name" style="left:95px;top:422px">Village Grocers</div>
    <div class="category-name" style="left:446px;top:422px">Butchers</div>
    <div class="category-name" style="left:797px;top:422px">Seafood</div>

    <footer class="site-footer" style="top:490px">
      <ul class="footer-links left"><li>Our Mission</li><li>Home Delivery</li><li>Contact</li></ul>
      <div class="footer-brand"><div class="brand-name">HOLMWYCK</div><div class="brand-tagline">Corvales Village</div></div>
      <ul class="footer-links right"><li>Join the Village</li><li>Friendwall</li><li>Snapgrid</li></ul>
    </footer>
  </section>

  <!-- Grocers -->
  <div class="page-label" style="top:769px">PAGE2</div>
  <section class="page" style="top:829px;height:624px">
    <div class="brand" style="top:46px">
      <div class="brand-name">HOLMWYCK</div>
      <div class="brand-tagline">Corvale's Online Shopping Village</div>
    </div>

    <div class="store-mark store-pdnq" style="left:450px;top:309px"><span class="mark-square"></span>PDNQ</div>
    <div class="store-mark store-mundey" style="left:831px;top:290px"><span class="mark-circle"></span>Mundey's Grocer</div>

    <footer class="site-footer" style="top:489px">
      <ul class="footer-links left"><li>Our Mission</li><li>Home Delivery</li><li>Contact</li></ul>
      <div class="footer-brand"><div class="brand-name">HOLMWYCK</div><div class="brand-tagline">Corvales Village</div></div>
      <ul class="footer-links right"><li>Join the Village</li><li>Friendwall</li><li>Snapgrid</li></ul>
    </footer>
  </section>

  <!-- Store -->
  <div class="page-label" style="top:1495px">PAGE3</div>
  <section class="page" style="top:1546px;height:985px">
    <div class="store-mark store-pdnq" style="left:600px;top:91px"><span class="mark-square"></span>PDNQ</div>

    <div class="frame" style="left:272px;top:189px"><span class="frame-post left"></span><span class="frame-post right"></span><div class="frame-photo photo-deli" role="img" aria-label="Cured meats and salami on a wooden board"></div></div>
    <div class="frame" style="left:616px;top:189px"><span class="frame-post left"></span><span class="frame-post right"></span><div class="frame-photo photo-fruitveg" role="img" aria-label="Fresh vegetables on a dark table"></div></div>
    <div class="frame" style="left:272px;top:508px"><span class="frame-post left"></span><span class="frame-post right"></span><div class="frame-photo photo-bakery" role="img" aria-label="Assorted bread loaves and rolls"></div></div>
    <div class="frame" style="left:616px;top:508px"><span class="frame-post left"></span><span class="frame-post right"></span><div class="frame-photo photo-pantry" role="img" aria-label="Shelves of preserved food in jars"></div></div>

    <div class="category-name" style="left:272px;top:449px">Deli Goods</div>
    <div class="category-name" style="left:616px;top:449px">Fruit &amp; Veg</div>
    <div class="category-name" style="left:272px;top:769px">Bakery</div>
    <div class="category-name" style="left:616px;top:769px">Pantry Items</div>

    <footer class="site-footer" style="top:838px">
      <ul class="footer-links left"><li>Our Mission</li><li>Home Delivery</li><li>Contact</li></ul>
      <div class="footer-brand"><div class="brand-name">HOLMWYCK</div><div class="brand-tagline">Corvales Village</div></div>
      <ul class="footer-links right"><li>Join the Village</li><li>Friendwall</li><li>Snapgrid</li></ul>
    </footer>
  </section>

</body>
</html>
```